Geschäftspapiere für Termin Startup
Zielgruppe
Wir sind ein Startup, das über die Seite Planorix.de (derzeit noch in der Beta-Phase)zukünftig folgenden Service anbietet: Unternehmer können sehr flexibel (selbst) gestaltete Terminformulare erstellen und auf Ihrer Website einbinden. Kunden können dann diese Termine buchen und bekommen dann Erinnerungs-Mails und SMS.
Zielgruppe: Dienstleister wie Fotografen, Friseure, Versicherungsvertreter, Masseure, Restaurants, Arztpraxen. Also alle, die darauf angewiesen sind, dass vereinbarte Termine eingehalten werden und die die Terminvereinbarung vereinfachen wollen. Also weniger per Telefon, mehr über die eigene Website.
Dateien bitte beachten für die Ansicht des Look & Feels:
https://ablage.beispielwolke.de/open?id=7QmrtHkWz2LpA94bNc3sVyTeOx8dGJuR_
Bonus-Aktion: Wir zahlen pauschal jeweils 30,00 Euro an die Designer auf den Plätzen 2 bis 4 für die geleistete Arbeit. Nur einer kann gewinnen und den Zuschlag bekommen. Aber so möchten wir gerne die Arbeit dennoch honorieren.
Aufgabenstellung
Wir benötigen ein modernes Briefpapier-Layout passend zu unserem CD.
Gerne darf/soll der ORBO (siehe Maskottchen in https://ablage.beispielwolke.de/open?id=5PwqNsYt8BaLmr2Hc7xkDuQOEPfjWzVbn )darauf erscheinen.
Maskottchen ORBO gibt es in mehreren Varianten. Siehe https://ablage.beispielwolke.de/ordner/8TrnWqLeHd5XcmZ3sJ4yPvBkGfQaNuRox?teilen=ja
Auch als Variante, das Maskottchen ORBO gegen das Logo gelehnt ist, kann genutzt werden: https://ablage.beispielwolke.de/open?id=3MuxBgTpW7RkaNj6yVqLeDsHcZoPfGtYi
Das Thema 'Terminvereinbarung' soll sofort erfasst werden mittels des Layouts bzw. der grafischen Elemente.
Auch die Branchen-Icons ( https://ablage.beispielwolke.de/ordner/6HpvRtNmQ2WkzLx8yEcBaJdFsUoGiTbeq?teilen=ja ) dürfen verwendet werden.

```html
<!DOCTYPE html>
<html lang="de">
<head>
<meta charset="utf-8">
<title>Planorix – Geschäftsausstattung</title>
<link href="https://fonts.googleapis.com/css2?family=Montserrat:wght@400;500;600&display=swap" rel="stylesheet">
<style>
  :root {
    --grey: #777c80;
    --grey-dark: #6a6f73;
    --green: #8cc63f;
    --ink: #2e2e2e;
    --paper: #ffffff;
    --shadow: 0 2px 6px rgba(0,0,0,.28);
  }
  * { box-sizing: border-box; margin: 0; padding: 0; }
  html, body { width: 1200px; height: 802px; overflow: hidden; background: #fff; }
  body { position: relative; font-family: "Montserrat", sans-serif; color: var(--ink); }

  .sheet { position: absolute; background: var(--paper); box-shadow: var(--shadow); overflow: hidden; }

  .brand { position: absolute; text-align: right; line-height: 1; }
  .brand-name { font-weight: 500; color: var(--green); display: flex; align-items: center; gap: .25em; justify-content: flex-end; white-space: nowrap; }
  .brand-square { width: .7em; height: .7em; background: var(--grey); display: inline-block; }
  .brand-tag { color: var(--grey); font-weight: 400; margin-top: .15em; white-space: nowrap; }
  .brand.on-grey .brand-name, .brand.on-grey .brand-tag { color: #fff; }
  .brand.on-grey .brand-square { background: #fff; }

  .contact { position: absolute; text-align: right; font-size: 6.4px; line-height: 1.2; white-space: nowrap; }
  .contact p + p { margin-top: 9px; }

  .mascot { position: absolute; border-radius: 40% 40% 30% 30%;
    background: radial-gradient(circle at 50% 45%, rgba(140,198,63,.85) 0%, rgba(122,181,52,.6) 45%, rgba(160,164,168,.3) 75%, rgba(255,255,255,0) 100%); }

  /* letterhead */
  .letterhead { left: 17px; top: 25px; width: 533px; height: 755px; }
  .letterhead .top-band { position: absolute; left: 0; top: 0; width: 100%; height: 8px; background: var(--grey); }
  .letterhead .brand { right: 23px; top: 17px; }
  .letterhead .brand-name { font-size: 33px; }
  .letterhead .brand-tag { font-size: 8px; }
  .letterhead .contact { right: 23px; top: 84px; }
  .return-line { position: absolute; left: 76px; top: 138px; font-size: 6.4px; white-space: nowrap; }
  .fold-mark { position: absolute; left: 5px; top: 257px; width: 7px; height: 1px; background: var(--ink); }
  .letterhead .mascot { left: 441px; top: 637px; width: 84px; height: 76px; }
  .letter-footer { position: absolute; left: 0; bottom: 0; width: 100%; height: 36px; background: var(--grey);
    border-top: 3px solid var(--green); display: flex; align-items: center; padding-left: 32px; color: #fff; font-size: 5.6px; line-height: 1.35; white-space: nowrap; }
  .letter-footer .col { padding: 0 11px; border-left: 1px solid rgba(255,255,255,.8); }
  .letter-footer .col:first-child { padding-left: 0; border-left: 0; }
  .letter-footer strong { font-weight: 600; }

  /* business cards */
  .card-back { left: 397px; top: 205px; width: 195px; height: 127px; background: var(--grey); }
  .card-back .brand { right: 17px; top: 50px; }
  .card-back .brand-name { font-size: 26px; }
  .card-back .brand-tag { font-size: 7px; }
  .card-band { position: absolute; left: 0; bottom: 0; width: 100%; height: 10px; background: var(--grey-dark); border-top: 2px solid var(--green); }

  .card-front { left: 397px; top: 357px; width: 195px; height: 126px; }
  .card-front .top-strip { position: absolute; left: 0; top: 0; width: 100%; height: 3px; background: var(--grey); }
  .card-front .brand { left: 15px; top: 14px; text-align: left; }
  .card-front .brand-name { font-size: 15px; justify-content: flex-start; }
  .card-front .brand-tag { font-size: 4px; padding-left: 40px; }
  .card-front .contact { right: 13px; top: 51px; font-size: 5.3px; }
  .card-front .contact p + p { margin-top: 7px; }
  .card-front .mascot { left: 15px; top: 64px; width: 38px; height: 42px; }

  /* envelope front */
  .envelope-front { left: 632px; top: 89px; width: 541px; height: 282px; }
  .envelope-front .top-band { position: absolute; left: 0; top: 0; width: 100%; height: 8px; background: var(--grey); }
  .envelope-front .brand { left: 50px; top: 30px; }
  .envelope-front .brand-name { font-size: 36px; }
  .envelope-front .brand-tag { font-size: 9px; }
  .address-window { position: absolute; left: 49px; top: 137px; width: 217px; height: 108px; border-radius: 8px;
    background: #ececec; box-shadow: inset 0 0 4px rgba(0,0,0,.25); }
  .envelope-front .bottom-band { position: absolute; left: 0; bottom: 0; width: 100%; height: 21px; background: var(--grey); border-top: 2px solid var(--green); }

  /* envelope back */
  .envelope-back { position: absolute; left: 631px; top: 411px; width: 537px; height: 331px; }
  .envelope-back svg { position: absolute; inset: 0; filter: drop-shadow(0 2px 4px rgba(0,0,0,.22)); }
  .envelope-back .mascot { left: 210px; top: 139px; width: 159px; height: 146px; }
  .envelope-back .brand { right: 22px; top: 294px; }
  .envelope-back .brand-name { font-size: 13px; }
  .envelope-back .brand-tag { font-size: 3.5px; }
</style>
</head>
<body>

<section class="sheet letterhead" aria-label="Briefbogen">
  <div class="top-band"></div>
  <div class="brand">
    <div class="brand-name"><span class="brand-square"></span>Planorix</div>
    <div class="brand-tag">Tool by termin-werk.com</div>
  </div>
  <div class="contact">
    <p>Lindenweg 48 · 34567 Beispielstadt</p>
    <p>Telefon: 0987/65 43 21-0<br>Fax: 0987/65 43 21-9</p>
    <p>E-Mail: info@planorix.de<br>Internet: www.planorix.de<br>www.treffpunkt-plan.de</p>
  </div>
  <p class="return-line">Planorix · Lindenweg 48 · D-34567 Beispielstadt</p>
  <span class="fold-mark"></span>
  <div class="mascot" role="img" aria-label="Maskottchen ORBO mit Terminkalender und Zauberstab"></div>
  <footer class="letter-footer">
    <div class="col">Bank: Beispiel Kreditbank AG, Nordstadt<br>IBAN: DExx 1111 2222 3333 4444 55</div>
    <div class="col">Registergericht Nordstadt HRB 00000<br>Geschäftsführender Gesellschafter: Jonas Beispielmann</div>
    <div class="col"><strong>Terminvereinbarung:</strong><br>Et dolor sit plique esti nonsed quias</div>
  </footer>
</section>

<section class="sheet card-back" aria-label="Visitenkarte Rückseite">
  <div class="brand on-grey">
    <div class="brand-name"><span class="brand-square"></span>Planorix</div>
    <div class="brand-tag">Tool by termin-werk.com</div>
  </div>
  <div class="card-band"></div>
</section>

<section class="sheet card-front" aria-label="Visitenkarte Vorderseite">
  <div class="top-strip"></div>
  <div class="brand">
    <div class="brand-name"><span class="brand-square"></span>Planorix</div>
    <div class="brand-tag">Tool by termin-werk.com</div>
  </div>
  <div class="mascot" role="img" aria-label="Maskottchen ORBO mit Terminkalender"></div>
  <div class="contact">
    <p>Lindenweg 48 · 34567 Beispielstadt</p>
    <p>Telefon: 0987/65 43 21-0<br>Fax: 0987/65 43 21-9</p>
    <p>E-Mail: info@planorix.de<br>Internet: www.planorix.de<br>www.treffpunkt-plan.de</p>
  </div>
  <div class="card-band"></div>
</section>

<section class="sheet envelope-front" aria-label="Briefumschlag Vorderseite">
  <div class="top-band"></div>
  <div class="brand">
    <div class="brand-name"><span class="brand-square"></span>Planorix</div>
    <div class="brand-tag">Tool by termin-werk.com</div>
  </div>
  <div class="address-window"></div>
  <div class="bottom-band"></div>
</section>

<section class="envelope-back" aria-label="Briefumschlag Rückseite">
  <svg width="537" height="331" viewBox="0 0 537 331">
    <path d="M4 64 L14 18 Q18 0 40 0 H497 Q519 0 523 18 L533 64 Z" fill="#f2f2f2"/>
    <rect x="44" y="6" width="449" height="24" fill="#fafafa"/>
    <path d="M0 64 Q28 64 30 78 L30 95 H507 L507 78 Q509 64 537 64 V331 H0 Z" fill="#e6e6e6"/>
    <path d="M2 100 Q2 80 30 80 H507 Q535 80 535 100 V331 H2 Z" fill="#f6f6f6"/>
    <rect x="22" y="118" width="493" height="210" fill="#fdfdfd"/>
  </svg>
  <div class="mascot" role="img" aria-label="Maskottchen ORBO mit Zauberhut, Kalender und Zauberstab"></div>
  <div class="brand">
    <div class="brand-name"><span class="brand-square"></span>Planorix</div>
    <div class="brand-tag">Tool by termin-werk.com</div>
  </div>
</section>

</body>
</html>
```